www.brevatin.com Sales/Order Page ReDesign

We need a new and amazing design for our sales/order page to attract more costumers and new houses for our portal.

Here is the existing page with the current design: https://www.brevatin.com/sales

We are proud owners of www.sommarhytta.no and www.brevatin.com and we want more holiday home owners to join our page so that we can rent out their holiday homes and increase the number of houses on our portal.

To get more homeowners we need a sales page that can sell our products the best way possible. Therefore we want you too blow us away with a fresh, modern, easy understandable and stylish new sales/order page.

The only restrictions we give when it comes to design is that it needs to fit the existing design of our portals, the top and footer are set. Beside that we are open for everything as long as it at once give the customers impression that this is a good, professional page were they just have to put out their houses.

When it comes to content I have added two documents who include the content to put in here and some guidelines on how to organize the page. Please be creative and add necessary graphics, symbols, background pictures and what ever necessary to make this page look professional and appealing to new costumers.

Looking forward to what suggestions we are given.

We just want to inform that we have updated our brief with a much more concrete description of what content to add on the sale page, and who to structure the content on the page. Hope this helps to make suggestions easier. Looking forward to receive some good contributions.

We would just like to make sure that everyone have understood that we are not asking for a new design suggestion to our portal in general. We are only asking for a redesign of our sales/order page you find here www.brevatin.com/sales. We have to day received some designs for our front page and the design it self was good, but that's not what we are asking for this time and don't want you to use time of something we don't need at the moment. We are looking forward too se some good suggestions.

Reason: Hello. Thanks for all the great contributions we have been given so fare. We haven't been able to respond to all design and are therefore extending the deadline so that we are able to respond to the designs we have been giver and to gov time to make final changes.

Reason: We are extending the deadline to give designers time to give new suggestion based on our latest feedback today.

Reason: Extended so we can receive last design changes.

Target Market(s)

This is a presentation page where we present our product agains new home owner who we what to choose listing there property on or site.

Industry/Entity Type

Sales

Requirements
Must have
• A modern design who calms the costumer down and help them in deciding to chose us, and for them to choose us they need to trust and believe in us. Therefore your main task is to create a page that effectively informs about our product, gets the visitors attentions and make them trust us.
Nice to have
• Examples of good competitors and good order pages we like:

http://www.cabinquest.example/info/lyp?icid=IL___O_Text___top_nav_link
https://www.nestlodge.example/rooms/new
https://www.pearvix.example/phone/compare/
http://www.guestnook.example/host
Should not have
• - Bad design :-). With bad design we mean design that looks like it's made in 2 seconds by a little child.

```html
<!DOCTYPE html>
<html lang="en">
<head>
<meta charset="utf-8">
<title>Brevatin – List your property</title>
<link href="https://fonts.googleapis.com/css2?family=Fjalla+One&family=Arimo:wght@400;700&display=swap" rel="stylesheet">
<style>
:root{
  --blue:#1a8fdc;
  --blue-dark:#0b74c4;
  --blue-head:#2e9fe6;
  --green:#a5cf3b;
  --green-dark:#86b22a;
  --slate:#3b4046;
  --slate-line:#555b62;
  --ink:#333;
  --muted:#666;
  --field:#c9c9c9;
  --red:#d42020;
  --white:#fff;
}
*{box-sizing:border-box;margin:0;padding:0}
html,body{width:1200px;height:2339px;overflow:hidden}
body{position:relative;font-family:"Arimo",Arial,sans-serif;color:var(--ink);background:#cfe3f3}
.scenery{position:absolute;left:0;top:0;width:1200px;height:2115px;
  background:linear-gradient(180deg,#3d8fd0 0%,#bcd8ee 18%,#e6eef4 45%,#8fb7d6 70%,#2e7fc0 88%,#1c64a8 100%)}
.topbar{position:absolute;left:0;top:0;width:1200px;height:48px;background:linear-gradient(#1380d2,#0f6fbd)}
.flags{position:absolute;left:670px;top:14px;display:flex;gap:8px}
.flag{width:30px;height:20px;display:block}
.signin{position:absolute;left:748px;top:8px;width:148px;height:36px;border-radius:4px;background:linear-gradient(#b4d95a,#8cbb2d);color:#2f4a0d;font-size:14px;font-weight:700;line-height:36px;padding-left:44px}
.signin::before{content:"";position:absolute;left:16px;top:12px;width:12px;height:12px;background:#4d6d16;border-radius:2px}
.signin::after{content:"";position:absolute;right:14px;top:16px;border:5px solid transparent;border-top-color:#4d6d16}
.list-link{position:absolute;left:908px;top:14px;color:#fff;font-weight:700;font-size:16px}
.logo-card{position:absolute;left:159px;top:0;width:310px;height:156px}
.logo-card svg{position:absolute;left:0;top:0}
.logo{position:absolute;left:28px;top:22px;display:flex;align-items:center;gap:14px}
.logo-mark{width:56px;height:56px;background:var(--blue)}
.logo-name{font-family:"Fjalla One",sans-serif;font-size:46px;color:var(--blue);line-height:1}

.panel{position:absolute;left:159px;top:179px;width:882px;height:1916px;background:rgba(255,255,255,.93)}
.compare{position:absolute;left:24px;top:0}
.col-head{position:absolute;text-align:center;color:#fff;font-family:"Fjalla One",sans-serif}
.h-flex{left:0;top:63px;width:252px;height:110px;background:var(--green);font-size:40px;line-height:48px;padding-top:6px}
.h-free{left:252px;top:45px;width:291px;height:128px;background:var(--blue);font-size:40px;line-height:48px;padding-top:16px}
.h-year{left:543px;top:24px;width:291px;height:149px;background:var(--slate);font-size:40px;line-height:48px;padding-top:38px}
.price{display:block;font-family:"Arimo",Arial,sans-serif;font-size:34px;line-height:44px}
.ribbon{position:absolute;left:736px;top:-12px;width:98px;height:72px}
.ribbon svg{position:absolute;left:0;top:0}
.ribbon span{position:absolute;left:0;width:98px;text-align:center;color:var(--red);font-weight:700;line-height:1}
.rows{position:absolute;left:0;top:173px;width:834px}
.row{display:grid;grid-template-columns:252px 291px 291px}
.row>div{padding:12px 12px;font-size:14.5px;line-height:18px;overflow:hidden}
.row+.row>div{border-top:1px solid rgba(255,255,255,.55)}
.row+.row .label{border-top:1px solid #5d636a}
.row .label{background:var(--slate);color:#fff;font-size:22px;line-height:26px;padding:10px 12px 0 24px;position:relative}
.row .label::before{content:"";position:absolute;left:0;top:16px;border:8px solid transparent;border-left-color:#fff}
.row .free{background:var(--green);color:#22340a}
.row .year{background:var(--blue);color:#fff}
.badge{display:inline-block;vertical-align:middle;width:130px;height:34px;border-radius:17px;background:#2aa3e8;margin-left:8px}
.badge.dark{background:#1979c6}
.plans{display:grid;grid-template-columns:100px 1fr;margin-top:10px;line-height:20px;white-space:nowrap}
.strike{text-decoration:line-through;margin-right:30px}

.section-title{position:absolute;left:44px;font-family:"Fjalla One",sans-serif;color:var(--blue);font-size:31px}
.btn{position:absolute;background:linear-gradient(#b6da5f,#8ebd2f);border:1px solid var(--green-dark);border-radius:3px;color:#2f4a0d;font-weight:700;font-size:15px;text-align:center}
.prop-table{position:absolute;left:44px;top:1058px;width:794px;border-collapse:collapse;font-size:15px}
.prop-table td,.prop-table th{border:1px solid #bbb;font-weight:400;text-align:left;padding:6px 8px}
.prop-table th{height:36px}
.prop-table .num{width:102px;text-align:center}
.select{height:30px;border:1px solid #aaa;background:#fff;position:relative;font-size:13px;line-height:28px;padding-left:10px;width:430px}
.select::after{content:"";position:absolute;right:0;top:0;width:30px;height:28px;background:var(--blue)}
.select::before{content:"";position:absolute;right:9px;top:11px;border:6px solid transparent;border-top-color:#fff;z-index:1}
.amount{color:var(--blue)}
.remove{color:var(--red);font-weight:700;margin-left:30px}
.total-label{text-align:right!important;font-size:20px;border-bottom:none}

.form{position:absolute;left:44px;top:1263px}
.field{position:absolute;left:0;font-size:15px;color:var(--ink);width:800px;height:34px}
.field span{position:absolute;left:2px;top:8px}
.input{position:absolute;top:0;height:32px;border:1px solid var(--field);background:#fff}

.terms{position:absolute;left:44px;top:1760px;width:800px;font-size:12.5px;color:var(--ink)}
.terms ul{list-style:none;margin-top:10px;font-size:11px;line-height:14px}
.terms li{padding-left:12px;position:relative}
.terms li::before{content:"";position:absolute;left:0;top:4px;border:4px solid transparent;border-left-color:var(--blue)}
.terms a{color:var(--red);font-style:italic}
.agree{position:absolute;left:44px;top:1845px;font-size:14px;display:flex;align-items:center;gap:10px}
.box{width:18px;height:18px;border:1px solid #999;background:#fff}

.footer{position:absolute;left:0;top:2115px;width:1200px;height:224px;background:linear-gradient(var(--blue-head),var(--blue-dark))}
.f-col{position:absolute;top:50px;color:#fff;font-size:12.5px}
.f-col h4{font-size:13.5px;margin-bottom:10px}
.f-col li{list-style:none;line-height:19px;padding-left:22px;position:relative}
.f-col li::before{content:"";position:absolute;left:0;top:3px;width:12px;height:12px;border-radius:50%;background:#fff}
.f-col.plain li::before{border-radius:0;width:10px;height:10px;top:4px}
.divider{position:absolute;top:40px;width:1px;height:150px;background:rgba(255,255,255,.3)}
.world{position:absolute;left:285px;top:47px;width:205px;height:100px;border-radius:30px;background:radial-gradient(ellipse at center,rgba(255,255,255,.85),rgba(255,255,255,.35) 60%,transparent 75%)}
</style>
</head>
<body>
<div class="scenery" role="img" aria-label="Background photo of a Norwegian fjord village with steep mountains under a bright sky"></div>

<header class="topbar">
  <div class="flags">
    <svg class="flag" viewBox="0 0 30 20" aria-label="Norwegian"><rect width="30" height="20" fill="#c8102e"/><rect x="8" width="6" height="20" fill="#fff"/><rect y="7" width="30" height="6" fill="#fff"/><rect x="9.5" width="3" height="20" fill="#00205b"/><rect y="8.5" width="30" height="3" fill="#00205b"/></svg>
    <svg class="flag" viewBox="0 0 30 20" aria-label="English"><rect width="30" height="20" fill="#012169"/><path d="M0 0L30 20M30 0L0 20" stroke="#fff" stroke-width="4"/><path d="M0 0L30 20M30 0L0 20" stroke="#c8102e" stroke-width="1.5"/><rect x="12" width="6" height="20" fill="#fff"/><rect y="7" width="30" height="6" fill="#fff"/><rect x="13.5" width="3" height="20" fill="#c8102e"/><rect y="8.5" width="30" height="3" fill="#c8102e"/></svg>
  </div>
  <div class="signin">Sign in</div>
  <div class="list-link">List your property</div>
</header>

<div class="logo-card">
  <svg width="310" height="156" viewBox="0 0 310 156">
    <polygon points="0,0 310,0 310,118 155,156 0,118" fill="#3b4046"/>
    <polygon points="0,0 310,0 310,98 155,134 0,98" fill="#fff"/>
  </svg>
  <div class="logo"><div class="logo-mark"></div><div class="logo-name">Brevatin</div></div>
</div>

<main class="panel">
  <section class="compare">
    <div class="col-head h-flex">Flexible<br>Advertising</div>
    <div class="col-head h-free">Free Advertising<span class="price">NOK 0.00</span></div>
    <div class="col-head h-year">Yearly Advertising<span class="price">NOK 4,990.00</span></div>
    <div class="ribbon">
      <svg width="98" height="84" viewBox="0 0 98 84"><polygon points="10,0 98,0 98,84 78,70 10,70" fill="#fff"/><polygon points="98,70 98,84 84,70" fill="#999"/></svg>
      <span style="top:14px;font-size:24px;font-weight:400">Special</span>
      <span style="top:40px;font-size:21px">OFFER</span>
    </div>

    <div class="rows">
      <div class="row" style="height:51px"><div class="label">Listing Fee</div><div class="free">No fixed fee for advertising.</div><div class="year">Pay a fixed yearly price for advertising. No limits on number of bookings.</div></div>
      <div class="row" style="height:89px"><div class="label">Running Cost</div><div class="free">Pay a provision, just 18% on the booking you receive. A transaction fee of 4.5% will be added.</div><div class="year">No provision. There is a transaction fee on 4.5%.</div></div>
      <div class="row" style="height:57px"><div class="label">Advertising</div><div class="free">You can advertise as long as you wish.</div><div class="year">You are guaranteed advertising for 12 months, from the publishing date.</div></div>
      <div class="row" style="height:61px"><div class="label">Number of Images:</div><div class="free">Upload an unlimited number of images of your property.</div><div class="year">Upload an unlimited number of images of your property.</div></div>
      <div class="row" style="height:147px"><div class="label">Broad Marketing:</div>
        <div class="free">Optional listing at: <span class="badge"></span>
          <div class="plans"><span>60 days</span><span>400 NOK</span><span>120 days</span><span>700 NOK</span><span>240 days</span><span>1 300 NOK</span><span>1 year</span><span><span class="strike">1 900 NOK</span>700 NOK</span></div></div>
        <div class="year">Optional listing at:<br><span class="badge dark" style="margin:16px 0 0 0"></span></div></div>
      <div class="row" style="height:118px"><div class="label">Your Own Housing Advisor:</div><div class="free">We are are concerned with your rental and advertising. You are assigned your personal advisor, which can advice and give recommendations to make your listing more atractive.</div><div class="year">We are are concerned with your rental and advertising. You are assigned your personal advisor, which can advice and give recommendations to make your listing more atractive.</div></div>
      <div class="row" style="height:109px"><div class="label">Relax And Wait For Bookings:</div><div class="free">Our call center is ready to assist your guests before, during and after the stay. You can use your time on important things, we'll take care of payments and administering your bookings.</div><div class="year">Our call center is ready to assist your guests before, during and after the stay. You can use your time on important things, we'll take care of payments and administering your bookings.</div></div>
      <div class="row" style="height:74px"><div class="label">Online Booking:</div><div class="free">Your property will be available for booking 24 hours a day, 7 days a week, 365 days a year.</div><div class="year">Your property will be available for booking 24 hours a day, 7 days a week, 365 days a year.</div></div>
      <div class="row" style="height:91px"><div class="label">Online Calendar:</div><div class="free">Your property will have an online calendar which is automatically maintained.</div><div class="year">Your property will have an online calendar which is automatically maintained.</div></div>
    </div>
  </section>

  <h2 class="section-title" style="top:1006px">Properties</h2>
  <div class="btn" style="left:647px;top:1005px;width:191px;height:45px;line-height:43px">+&nbsp; Add new property</div>
  <table class="prop-table">
    <tr><th class="num">Property no</th><th>Agreement</th><th style="width:226px"></th></tr>
    <tr><td class="num" rowspan="2" style="vertical-align:top;padding-top:4px">1</td><td style="height:50px"><div class="select">Yearly advertising, includes listing at Tunet.no (4990,-)</div></td><td><span class="amount">4990.00</span><span class="remove">✕</span></td></tr>
    <tr><td class="total-label" style="height:44px">Total</td><td>4990.00</td></tr>
  </table>

  <h2 class="section-title" style="top:1200px">Customer Details</h2>
  <form class="form">
    <div class="field" style="top:0"><span>Customer type</span><div class="input" style="left:164px;width:433px"></div></div>
    <div class="field" style="top:55px"><span>First name</span><div class="input" style="left:164px;width:433px"></div></div>
    <div class="field" style="top:110px"><span>Last name</span><div class="input" style="left:164px;width:433px"></div></div>
    <div class="field" style="top:165px"><span>Address</span><div class="input" style="left:164px;width:102px"></div><div class="input" style="left:274px;width:323px"></div></div>
    <div class="field" style="top:222px"><span>Postno/-place</span><div class="input" style="left:164px;width:433px"></div></div>
    <div class="field" style="top:277px"><span>E-mail</span><div class="input" style="left:164px;width:433px"></div></div>
    <div class="field" style="top:332px"><span>Confirm e-mail</span><div class="input" style="left:164px;width:433px"></div></div>
    <div class="field" style="top:389px"><span>Phone</span><div class="input" style="left:164px;width:102px"></div><div class="input" style="left:274px;width:323px"></div></div>
  </form>

  <h2 class="section-title" style="top:1708px">Terms</h2>
  <div class="terms">
    <p>We in Brevatin Holiday Rental ask you to confirm the following details before entering a legally binding contract.</p>
    <ul>
      <li>I hereby declare that I'm over 18 years of age.</li>
      <li>I'm agree to have my IP-address recorded with this booking.</li>
      <li>This is a norwegian corporation, with norwegian rules for e-commerce.</li>
      <li>I've read, understood and accept the <a>terms and conditions</a></li>
    </ul>
  </div>
  <div class="agree"><span class="box"></span>I've read, understood and agree the terms for this order</div>
  <div class="btn" style="left:695px;top:1818px;width:143px;height:45px;line-height:43px">Confirm order</div>
</main>

<footer class="footer">
  <div class="f-col" style="left:173px"><h4>Destinations</h4><ul><li>Europe</li><li>North America</li><li>South America</li><li>Africa</li><li>Asia</li><li>Australia</li></ul></div>
  <div class="world" role="img" aria-label="World map"></div>
  <div class="divider" style="left:508px"></div>
  <div class="f-col" style="left:525px"><h4>For tenants</h4><ul><li>My page</li><li>Why Brevatin?</li><li>Help</li><li>Rental terms</li></ul></div>
  <div class="divider" style="left:665px"></div>
  <div class="f-col" style="left:683px"><h4>For house owners</h4><ul><li>MyAdmin</li><li>Let us rent your house</li><li>Conditions</li></ul></div>
  <div class="divider" style="left:868px"></div>
  <div class="f-col plain" style="left:887px;top:42px"><h4>Contact us</h4><ul><li style="padding-left:22px">Brevatin Holiday Rental</li><li>post@brevatin.com</li><li>+47 55 10 20 30</li><li>www.brevatin.com</li></ul>
    <h4 style="margin-top:8px">Opening hours</h4><ul><li>Mon - Fri: 9.00 AM - 5.00 PM</li><li>Sat - Sun: Closed</li></ul></div>
</footer>
</body>
</html>
```